Book Cover Design - Rooted Together: 7 Paths to Raise a Home that Flourishes

International cover needed for the Australian (Marlow Fenwick/QRT Press 2011) non-fiction book Rooted Together: 7 Paths to Raise a Home that Flourishes.

Blurb: With the birth of a baby, come other new beginnings, the birth of a mother, of a father, and of a family. With each stage of a child's growth, and with every new baby, there are more new beginnings. In older cultures and in villages around the world, parenthood was considered a rite of passage but traditions that guided parents into becoming a family have largely been lost - until now.

This ground breaking book walks a new generation of mothers and fathers through the eight steps of the modern parenthood rite of passage, from couple-connection to family-foundations, so they can prepare for and continue to grow a family that thrives.

Bio: Mara Quinlan is a relationship counsellor, parent educator and columnist for Sensible Homelife magazine. She lives in Sydney with her husband, their three gorgeous children and an itinerary of pets. This is her first book.
Updates

Thank you for your patience, I haven't ever done anything like this before and the designs submitted have helped me to be more specific in my requests. Please see the updated brief. The most important point is that I am seeking a TEXT based cover, so BOTH the TITLE and SUBTITLE should take up most of the space, the image could either be in the background with the title and subtitle overlayed, or be much smaller to fit around them. I have attached some more images to the brief, hope they help to convey the 'feel' I am after.  Thanks again!

Reason: Thank you so much for taking an interest in this project, the process has been very educational and helpful for me. While some of the stock art in the submitted designs are great, I've decided to commission a custom illustration which completely captures the meaning of Rooted Together. I will upload the illustration once it's complete for designers who are still interested to use. Thank you for your patience! Mara

Thank you all for your patience and for opening up my thinking about what I am really hoping for with this cover. I have uploaded some new tree designs and more specific instructions that I would like to be included in the cover design. I'm looking forward to seeing your creations!

With warm regards,

Mara

Target Market(s)

Couples thinking about having a baby and new parents of one or more young children.

Industry/Entity Type

Baby

Requirements
Must have
• TEXT based cover with BOTH the TITLE and SUBTITLE taking up most of the page.
Colors to match the Australian version (see attached)
Tree design bottom left (as per Trunk Treatment image attached) OR Heart Tree Design
Root design (as per one of the two images attached)
PLEASE ADD: three new shoots coming up from the ground under the tree to symbolize the children.
Nice to have
• Artistic effect to complement Australian cover.
Subtle retro feel to complement Australian cover.
Should not have
• The book is inclusive of all parents (including same-sex parents) so no images of mother/father and baby.

```html
<!DOCTYPE html>
<html lang="en">
<head>
<meta charset="utf-8">
<title>Rooted Together – Book Cover</title>
<link rel="stylesheet" href="https://fonts.googleapis.com/css2?family=Alfa+Slab+One&family=Gilda+Display&family=Noto+Serif:wght@400;700&family=Oranienbaum&family=Pinyon+Script&family=Playfair+Display:ital,wght@0,400;1,400;1,700&display=swap">
<style>
  :root {
    --back-teal: #4b9786;
    --blurb-disc: #b6dfe0;
    --sky-top: #6bbfc8;
    --sky-mid: #a9d9d6;
    --meadow: #a6d17a;
    --cream: #f8efd8;
    --ink: #3a2a26;
    --red: #c33a2c;
    --teal-title: #4a958f;
    --mustard: #c9a12c;
    --white: #ffffff;
    --leaf-teal: #4fa3a8;
    --leaf-green: #7cbf4a;
  }
  html, body {
    margin: 0;
    padding: 0;
    width: 1200px;
    height: 864px;
    overflow: hidden;
    background: #ffffff;
  }
  .cover {
    position: relative;
    width: 1200px;
    height: 864px;
    overflow: hidden;
  }

  /* Back cover */
  .back {
    position: absolute;
    left: 0; top: 0;
    width: 578px; height: 864px;
    background: var(--back-teal);
  }
  .blurb-disc {
    position: absolute;
    left: 48px; top: 48px;
    width: 524px; height: 524px;
    border-radius: 50%;
    background: var(--blurb-disc);
  }
  .blurb {
    position: absolute;
    left: 88px; top: 172px;
    width: 444px;
    text-align: center;
    color: var(--ink);
  }
  .blurb-lead {
    margin: 0 52px 10px;
    font-family: "Alfa Slab One", serif;
    font-size: 16px;
    line-height: 24px;
    letter-spacing: 0.3px;
  }
  .blurb p.body {
    margin: 0 18px 8px;
    font-family: "Noto Serif", serif;
    font-size: 12.5px;
    line-height: 26px;
  }
  .blurb strong {
    font-family: "Alfa Slab One", serif;
    font-weight: 400;
  }
  .bio {
    position: absolute;
    left: 110px; top: 640px;
    width: 400px;
    margin: 0;
    text-align: center;
    color: var(--white);
    font-family: "Noto Serif", serif;
    font-size: 12.5px;
    line-height: 25px;
  }
  .bio strong { font-weight: 700; }

  /* Spine + front share one sky */
  .sky {
    position: absolute;
    left: 578px; top: 0;
    width: 622px; height: 864px;
    background: linear-gradient(180deg, var(--sky-top) 0%, var(--sky-mid) 48%, var(--meadow) 100%);
  }
  .spine {
    position: absolute;
    left: 578px; top: 0;
    width: 42px; height: 864px;
  }
  .spine-title {
    position: absolute;
    left: 34px; top: 30px;
    transform-origin: 0 0;
    transform: rotate(90deg);
    white-space: nowrap;
    font-family: "Gilda Display", serif;
    font-size: 21px;
    color: var(--ink);
  }
  .spine-title .lead { color: var(--red); }
  .spine-author {
    position: absolute;
    left: 33px; top: 628px;
    transform-origin: 0 0;
    transform: rotate(90deg);
    white-space: nowrap;
    font-family: "Gilda Display", serif;
    font-size: 21px;
    letter-spacing: 3px;
    color: var(--white);
  }

  .front-art {
    position: absolute;
    left: 0; top: 0;
  }
  .author-name {
    font-family: "Gilda Display", serif;
    font-size: 58px;
    letter-spacing: 5px;
    fill: var(--white);
  }
  .title-rooted {
    font-family: "Playfair Display", serif;
    font-style: italic;
    font-size: 104px;
    fill: var(--ink);
  }
  .title-together {
    font-family: "Oranienbaum", serif;
    font-size: 80px;
    fill: var(--red);
  }
  .numeral {
    font-family: "Playfair Display", serif;
    font-size: 270px;
    fill: none;
    stroke: var(--white);
    stroke-width: 3;
  }
  .numeral-dots {
    font-family: "Playfair Display", serif;
    font-size: 270px;
    fill: none;
    stroke: var(--white);
    stroke-width: 3;
    stroke-dasharray: 1 6;
    stroke-linecap: round;
  }
  .path-tile { fill: var(--mustard); }
  .path-letter {
    font-family: "Alfa Slab One", serif;
    font-size: 26px;
    fill: var(--white);
    text-anchor: middle;
  }
  .word-to {
    font-family: "Gilda Display", serif;
    font-size: 70px;
    fill: var(--ink);
  }
  .word-raise {
    font-family: "Oranienbaum", serif;
    font-size: 118px;
    fill: var(--teal-title);
  }
  .word-home {
    font-family: "Playfair Display", serif;
    font-style: italic;
    font-weight: 700;
    font-size: 32px;
    fill: var(--ink);
  }
  .word-home .plain {
    font-style: normal;
    font-weight: 400;
  }
  .word-flourishes {
    font-family: "Pinyon Script", cursive;
    font-size: 96px;
    fill: var(--ink);
  }
</style>
</head>
<body>
<div class="cover">

  <section class="back">
    <div class="blurb-disc"></div>
    <div class="blurb">
      <p class="blurb-lead">With the birth of a baby, come other new beginnings, the birth of a mother, of a father, and of a family.</p>
      <p class="body">With each stage of a child's growth, and with every new baby, there are more new beginnings. In older cultures and in villages around the world, parenthood was considered a rite of passage but traditions that guided parents into becoming a family have largely been lost - until now.</p>
      <p class="body">This ground breaking book walks a new generation of mothers and fathers through the eight steps of the modern parenthood rite of passage, from couple-connection to family-foundations, so they can prepare for and continue to grow <strong>a family that thrives</strong>.</p>
    </div>
    <p class="bio"><strong>Mara Quinlan</strong> is a relationship counsellor, parent educator and columnist for Sensible Homelife magazine. She lives in Sydney with her husband, their three gorgeous children and an itinerary of pets. This is her first book.</p>
  </section>

  <div class="sky"></div>

  <section class="spine">
    <div class="spine-title"><span class="lead">Rooted Together:</span> 7 Paths to Raise a Home that Flourishes</div>
    <div class="spine-author">MARA QUINLAN</div>
  </section>

  <svg class="front-art" width="1200" height="864" viewBox="0 0 1200 864">
    <g role="img" aria-label="Teal leafy branch reaching in from the top right corner">
      <ellipse cx="1150" cy="70" rx="70" ry="80" fill="var(--leaf-teal)" opacity="0.55"/>
    </g>
    <g role="img" aria-label="Faint teal leafy branch reaching in from the left edge">
      <ellipse cx="720" cy="320" rx="110" ry="70" fill="var(--leaf-teal)" opacity="0.35"/>
    </g>

    <circle class="sun-disc" cx="998" cy="275" r="165" fill="var(--cream)"/>

    <text class="author-name" x="912" y="80" text-anchor="middle">MARA QUINLAN</text>

    <text class="title-rooted" x="660" y="220">Rooted</text>
    <text class="title-together" x="998" y="392" text-anchor="middle" textLength="310" lengthAdjust="spacingAndGlyphs">TOGETHER:</text>
    <g class="rule-lines" fill="var(--ink)">
      <rect x="905" y="404" width="145" height="4"/>
      <rect x="905" y="413" width="145" height="3"/>
      <rect x="905" y="421" width="145" height="2"/>
    </g>

    <text class="numeral-dots" x="668" y="582">7</text>
    <text class="numeral" x="680" y="575">7</text>

    <rect class="path-tile" x="868" y="530" width="62" height="45"/>
    <text class="path-letter" x="899" y="562">p</text>
    <rect class="path-tile" x="915" y="502" width="70" height="30"/>
    <text class="path-letter" x="950" y="526">a</text>
    <rect class="path-tile" x="985" y="530" width="60" height="45"/>
    <text class="path-letter" x="1015" y="562">t</text>
    <rect class="path-tile" x="1040" y="502" width="62" height="30"/>
    <text class="path-letter" x="1071" y="526">h</text>
    <rect class="path-tile" x="1075" y="530" width="60" height="45"/>
    <text class="path-letter" x="1105" y="562">s</text>

    <path d="M965 628 C940 610 930 595 940 585 C950 576 962 582 965 592 C968 582 980 576 990 585 C1000 595 990 610 965 628 Z" fill="var(--red)"/>
    <path d="M965 634 C935 613 924 596 936 582 C948 571 961 577 965 585 C969 577 982 571 994 582 C1006 596 995 613 965 634 Z" fill="none" stroke="var(--red)" stroke-width="1.5" stroke-dasharray="3 3"/>

    <text class="word-to" x="1005" y="648">to</text>
    <text class="word-raise" x="628" y="698">Raise</text>
    <text class="word-home" x="905" y="700">a Home <tspan class="plain">that</tspan></text>
    <text class="word-flourishes" x="1185" y="808" text-anchor="end">Flourishes</text>

    <g role="img" aria-label="Green sprouting stem with leaves rising from the bottom edge">
      <ellipse cx="745" cy="810" rx="60" ry="70" fill="var(--leaf-green)" opacity="0.6"/>
    </g>
  </svg>

</div>
</body>
</html>
```